Irrigation company needing wrap for 4 fleet vehicles

We are a growing irrigation company in Arizona and are looking to improve our brand and professionalism. We had a logo designed a few years ago but never came up with a solid wrap design for the trucks. I don't know if this effects the design or not, but 2 trucks are Brenton Vael 2200 Crew Cab. 1 truck is Brenton Vael 2200 Quad Cab. 1 truck is Brenton Vael 2200 Standard Cab. We are the top in our industry and want to appear different from the competition. Professionalism, quality, honesty are the messages we're trying to show. Our website, ROC number, and phone should be listed. Our company logo is attached.

Industry/Entity Type

Lawn Care

Requirements
Must have
• Website - sunmeadowflowqx.com
ROC Number - 318072
Phone - 480-555-0137

```html
<!DOCTYPE html>
<html lang="en">
<head>
<meta charset="utf-8">
<title>Sunmeadow Flow – Fleet Wrap</title>
<link href="https://fonts.googleapis.com/css2?family=Poppins:wght@500;700&family=Oswald:wght@700&display=swap" rel="stylesheet">
<style>
  :root{
    --brand-blue:#1f86d1;
    --brand-green:#8cc63f;
    --stripe-black:#222426;
    --panel-white:#ffffff;
    --panel-edge:#d9dde1;
    --cream:#eef3e2;
    --ink:#111315;
  }
  html,body{margin:0;padding:0;overflow:hidden;background:#fff;}
  .wrap-sheet{position:relative;width:1200px;height:400px;overflow:hidden;background:#fff;}
  .view{position:absolute;}
  .side-left{left:40px;top:40px;width:380px;height:135px;}
  .side-right{left:800px;top:40px;width:380px;height:135px;}
  .tailgate{left:525px;top:65px;width:160px;height:60px;}
  .roof{left:55px;top:235px;width:300px;height:115px;}
  .hood-small{left:440px;top:235px;width:150px;height:130px;}
  .hood-large{left:660px;top:195px;width:250px;height:200px;}
  svg{display:block;width:100%;height:100%;}
  .web{font-family:'Poppins',sans-serif;font-weight:500;fill:var(--panel-white);}
  .phone{font-family:'Poppins',sans-serif;font-weight:700;fill:var(--panel-white);letter-spacing:.5px;}
  .brand-name{font-family:'Poppins',sans-serif;font-weight:700;fill:var(--brand-blue);}
  .tagline{font-family:'Oswald',sans-serif;font-weight:700;fill:var(--ink);letter-spacing:.3px;}
  .roc-label{font-family:'Oswald',sans-serif;font-weight:700;fill:var(--panel-white);letter-spacing:1px;}
  .roc-number{font-family:'Oswald',sans-serif;font-weight:700;fill:var(--brand-green);}
  .badge-text{font-family:'Poppins',sans-serif;font-weight:700;fill:var(--panel-white);}
</style>
</head>
<body>
<main class="wrap-sheet">

  <svg width="0" height="0" style="position:absolute">
    <defs>
      <clipPath id="truck-body">
        <path d="M4,34 L150,34 L154,6 L236,6 L278,32 L368,36 Q378,38 378,50 L378,112 Q378,120 370,120 L12,120 Q4,120 4,112 Z"/>
      </clipPath>
      <g id="side-graphics">
        <path class="body-panel" d="M4,34 L150,34 L154,6 L236,6 L278,32 L368,36 Q378,38 378,50 L378,112 Q378,120 370,120 L12,120 Q4,120 4,112 Z" fill="var(--panel-white)" stroke="var(--panel-edge)"/>
        <g clip-path="url(#truck-body)">
          <polygon class="upper-band" points="0,36 156,36 156,0 215,0 195,24 176,64 0,64" fill="var(--brand-blue)"/>
          <polygon class="cab-stripe" points="218,4 240,4 224,22 202,22" fill="var(--stripe-black)"/>
          <polygon class="diag-stripe" points="203,40 222,40 194,80 175,80" fill="var(--stripe-black)"/>
          <polygon class="lower-band" points="0,98 190,98 168,120 0,120" fill="var(--brand-blue)"/>
          <g class="dash-stripes" fill="var(--brand-green)">
            <polygon points="8,84 20,84 17,90 5,90"/>
            <polygon points="26,84 50,84 47,90 23,90"/>
            <polygon points="110,84 128,84 125,90 107,90"/>
            <polygon points="136,84 168,84 165,90 133,90"/>
            <polygon points="316,84 328,84 325,90 313,90"/>
            <polygon points="336,84 376,84 373,90 333,90"/>
          </g>
        </g>
      </g>
    </defs>
  </svg>

  <!-- Driver side panel -->
  <div class="view side-left">
    <svg viewBox="0 0 380 135">
      <use href="#side-graphics"/>
      <text class="web" x="20" y="48" font-size="6">sunmeadowflowqx.com</text>
      <text class="phone" x="20" y="58" font-size="8">480-555-0137</text>
      <text class="brand-name" x="262" y="80" font-size="16" text-anchor="middle">Sunmeadow</text>
      <text class="brand-name" x="262" y="98" font-size="16" text-anchor="middle">Flow</text>
    </svg>
  </div>

  <!-- Tailgate -->
  <div class="view tailgate">
    <svg viewBox="0 0 160 60">
      <rect x="0" y="0" width="160" height="60" fill="var(--panel-white)" stroke="var(--panel-edge)"/>
      <rect class="tailgate-band" x="0" y="0" width="160" height="34" fill="var(--brand-blue)"/>
      <rect class="logo-plate" x="6" y="4" width="44" height="26" fill="var(--panel-white)"/>
      <text class="brand-name" x="28" y="15" font-size="6.5" text-anchor="middle">Sunmeadow</text>
      <text class="brand-name" x="28" y="24" font-size="6.5" text-anchor="middle">Flow</text>
      <text class="web" x="150" y="14" font-size="6" text-anchor="end">sunmeadowflowqx.com</text>
      <text class="phone" x="150" y="26" font-size="9" text-anchor="end">480-555-0137</text>
      <g fill="var(--brand-green)">
        <polygon points="3,44 24,44 21,50 0,50"/>
        <polygon points="138,44 160,44 157,50 135,50"/>
      </g>
      <text class="tagline" x="80" y="50" font-size="8" text-anchor="middle">IRRIGATION SPECIALISTS</text>
    </svg>
  </div>

  <!-- Passenger side panel -->
  <div class="view side-right">
    <svg viewBox="0 0 380 135">
      <use href="#side-graphics" transform="translate(380,0) scale(-1,1)"/>
      <text class="web" x="360" y="48" font-size="6" text-anchor="end">sunmeadowflowqx.com</text>
      <text class="phone" x="360" y="58" font-size="8" text-anchor="end">480-555-0137</text>
      <text class="brand-name" x="118" y="80" font-size="16" text-anchor="middle">Sunmeadow</text>
      <text class="brand-name" x="118" y="98" font-size="16" text-anchor="middle">Flow</text>
    </svg>
  </div>

  <!-- Roof with ROC number -->
  <div class="view roof">
    <svg viewBox="0 0 300 115">
      <rect x="0" y="0" width="300" height="115" rx="10" fill="var(--panel-white)" stroke="var(--panel-edge)"/>
      <rect class="roof-band" x="133" y="5" width="55" height="105" fill="var(--brand-blue)"/>
      <rect class="roc-plate" x="141" y="22" width="15" height="72" fill="var(--panel-white)"/>
      <text class="roc-number" transform="translate(144,58) rotate(90)" font-size="12" text-anchor="middle">318072</text>
      <text class="roc-label" transform="translate(162,58) rotate(90)" font-size="9" text-anchor="middle">ROC NUMBER</text>
    </svg>
  </div>

  <!-- Hood, angled view -->
  <div class="view hood-small">
    <svg viewBox="0 0 150 130">
      <path class="hood-green" d="M70,10 Q120,20 140,60 Q145,100 120,120 L70,120 Q85,65 70,10Z" fill="var(--brand-green)"/>
      <circle cx="115" cy="65" r="24" fill="var(--cream)" stroke="var(--brand-blue)" stroke-width="1"/>
      <g transform="translate(115,65) rotate(90)">
        <text class="brand-name" x="0" y="-1" font-size="6.5" text-anchor="middle">Sunmeadow</text>
        <text class="brand-name" x="0" y="7" font-size="6.5" text-anchor="middle">Flow</text>
      </g>
      <circle cx="97" cy="83" r="6" fill="var(--brand-blue)"/>
    </svg>
  </div>

  <!-- Hood, front view -->
  <div class="view hood-large">
    <svg viewBox="0 0 250 200">
      <path class="hood-green" d="M45,20 Q125,0 205,20 L165,195 Q125,205 85,195Z" fill="var(--brand-green)"/>
      <circle cx="125" cy="130" r="48" fill="none" stroke="var(--ink)" stroke-width=".8"/>
      <circle cx="125" cy="130" r="38" fill="var(--cream)"/>
      <text class="brand-name" x="125" y="128" font-size="11" text-anchor="middle">Sunmeadow</text>
      <text class="brand-name" x="125" y="141" font-size="11" text-anchor="middle">Flow</text>
      <circle cx="90" cy="90" r="16" fill="var(--brand-blue)"/>
      <text class="badge-text" x="90" y="89" font-size="3.6" text-anchor="middle">IRRIGATION</text>
      <text class="badge-text" x="90" y="95" font-size="3.6" text-anchor="middle">SPECIALISTS</text>
    </svg>
  </div>

</main>
</body>
</html>
```